Clinician Supply Circle

I am a financial planner whose client's are physicians and dentists. As physicians, there is very little time for them to do research on numerous aspects of their business and personal lives. I am looking to build a website that is a 1 stop shop for many of the services/resources they may need. It will be my job to screen the resources/advertisers and place competent people/business's that I know and have a track record on. there will ultimately be 10 or 12 ish areas that I would like to provide resources in:
disability insurance
life insurance
retirement planning
student loan advisors
employment contract and business formation attorneys
accountants
real estate agents
physician mortgages
personal loans
malpractice insurance
physician recruiters
maybe 2 other areas which I have yet to figure out.....
I would like each of these options to be able to be clicked on and a page will open up with the 1 or 2 or 3 or 4 people/business's that I have picked to represent these areas. I would like each specific person/business to have a click here to contact me link in which an email goes to the person and I am copied on the initial correspondence between the physician and the mortgage broker.... just so I can see some of the correspondence they will be receiving.
nowhere on the site do I want it to say my name. there will be certain disclosures that are needed and other wording but I think this is a good starting point.
here are links to two websites with the same general concept. please keep in mind that I want my website to be more on the simple side.
http://www.quillbarrowpartners.example/index.html
http://fernlakeledger.example/
Updates
Industry/Entity Type
Financial

```html
<!DOCTYPE html>
<html lang="en">
<head>
<meta charset="utf-8">
<title>Clinician Supply Circle</title>
<link rel="stylesheet" href="https://fonts.googleapis.com/css2?family=Roboto:ital,wght@0,300;0,400;0,500;0,700;1,400&family=Open+Sans:wght@400;600;700&display=swap">
<style>
:root{
  --navy:#0b2641;
  --navy-2:#163a60;
  --lime:#c4d21a;
  --orange:#f29a0e;
  --orange-dark:#e5780c;
  --page:#ececec;
  --white:#ffffff;
  --ink:#333a40;
  --footer:#333333;
  --footer-low:#4d4d4d;
  --strip:#dcdcdc;
}
*{box-sizing:border-box;margin:0;padding:0}
html,body{width:776px;height:1200px;overflow:hidden}
body{background:var(--page);font-family:"Roboto",Arial,sans-serif;color:var(--ink);position:relative}
.abs{position:absolute}
a{color:inherit;text-decoration:none}

/* top bar */
.topbar{left:0;top:0;width:776px;height:22px;background:var(--navy)}
.topbar .contact{top:6px;font-size:8.5px;color:#d8dee6;display:flex;align-items:center;gap:4px}
.topbar .social{top:4px;left:584px;display:flex;gap:6px}
.topbar .social span{width:15px;height:15px;border:1px solid #7c8ea3;display:block}

/* header */
.header{left:0;top:22px;width:776px;height:64px;background:var(--white)}
.brand{left:111px;top:10px;display:flex;align-items:center;gap:8px}
.brand .mark{width:46px;height:46px;border-radius:50%;background:var(--navy)}
.brand .name{font-weight:700;font-size:14px;color:var(--navy);line-height:1}
.nav{top:25px;left:343px;height:39px;display:flex;font-size:9.5px;color:#2b3a48}
.nav a{display:flex;align-items:flex-start;justify-content:center;padding-top:6px}
.nav .current{background:var(--navy);color:#fff;width:48px;border-radius:3px 3px 0 0}

/* hero */
.hero{left:0;top:86px;width:776px;height:249px;background:var(--navy)}
.hero-panel{left:111px;top:92px;width:158px;height:243px;background:var(--lime);padding:22px 0 0 9px;color:#fff}
.hero-title{font-size:21px;line-height:23px;letter-spacing:-.4px;white-space:nowrap}
.hero-title b{font-weight:700;display:block}
.hero-title span{font-weight:300;display:block}
.hero-text{margin-top:8px;font-size:8.2px;line-height:11px;color:var(--navy);width:140px}
.hero-btn{margin-top:9px;width:138px;height:20px;background:linear-gradient(#f7a519,var(--orange-dark));font-size:8.5px;font-weight:700;display:flex;align-items:center;justify-content:center;gap:5px;border-radius:2px}
.dots{margin-top:10px;display:flex;gap:3px;margin-left:2px}
.dots i{width:7px;height:7px;border-radius:50%;background:#dfe6a8;border:1px solid #fff;display:block}
.dots i:first-child{background:var(--navy-2)}
.hero-photo{left:270px;top:92px;width:395px;height:243px;background:linear-gradient(115deg,#c9d6e3 0%,#e9eef2 45%,#b7c3cf 100%)}

/* main panel */
.main{left:111px;top:335px;width:554px;height:613px;background:#fff;box-shadow:0 0 6px rgba(0,0,0,.12)}
.welcome h1{position:absolute;left:0;top:22px;width:554px;text-align:center;font-size:17.5px;font-weight:700;color:var(--navy)}
.welcome p{position:absolute;left:24px;width:506px;text-align:center;font-size:7.8px;line-height:11px;color:#3c4248}
.more-btn{left:248px;top:129px;width:59px;height:20px;border:1px solid var(--navy);border-radius:4px;font-size:8px;font-weight:700;color:var(--navy);display:flex;align-items:center;justify-content:center;gap:3px}
.ring{width:7px;height:7px;border-radius:50%;background:var(--orange);display:inline-block}

.services{left:0;top:162px;width:554px;height:187px;background:var(--lime)}
.services h2{position:absolute;top:12px;width:554px;text-align:center;color:#fff;font-size:16px;font-weight:500}
.card{position:absolute;top:43px;width:108px;height:116px;background:#fff}
.card .cap{position:absolute;left:0;top:0;width:108px;height:16px;background:var(--navy)}
.card .icon{position:absolute;left:40px;top:28px;width:29px;height:29px;border-radius:50%;background:var(--orange)}
.card .label{position:absolute;top:63px;width:108px;text-align:center;font-size:10.5px;font-weight:700;line-height:13px;color:var(--navy)}
.card.hover{background:#555}
.card.hover .veil{position:absolute;inset:0;background:rgba(40,40,40,.82)}
.card.hover .label{color:#6e6e6e}
.arrow{position:absolute;top:82px;width:12px;height:23px;background:var(--navy);display:flex;align-items:center;justify-content:center}

.col-title{font-size:16px;font-weight:700;color:var(--navy)}
.post{position:absolute;left:18px;width:166px}
.post .date{font-size:6.8px;font-style:italic;color:#222}
.post .title{font-size:7.8px;color:var(--orange);margin-top:3px}
.post .text{font-size:7.4px;color:#555;line-height:11px;margin-top:2px}
.post-rule{position:absolute;left:18px;width:160px;border-top:1px dashed #bbb}
.news{position:absolute;left:198px;width:168px}
.news .tag{width:35px;height:12px;background:#b9b9b9;color:#fff;font-size:6.5px;display:flex;align-items:center;justify-content:center}
.news .text{font-size:7.2px;line-height:10.5px;color:#4b3a78;margin-top:6px}
.news .read{font-size:7.2px;color:var(--navy);margin-top:2px}
.promo{position:absolute;left:375px;width:160px;height:58px;border:1px solid #d4d4d4;border-radius:4px;background:linear-gradient(#fff,#ececec);text-align:center;padding-top:8px}
.promo h3{font-size:12.5px;font-weight:400;color:#1f2327}
.promo p{font-size:7.6px;line-height:10px;color:#555;margin-top:3px}
.promo.active{background:linear-gradient(#1c4f85,var(--navy));border-color:#9fb3c8}
.promo.active h3{color:#fff}
.promo.active p{color:#d9e2ec}

/* partners */
.partners{left:111px;top:948px;width:554px;height:70px;background:var(--strip)}
.partner{position:absolute;top:8px;width:84px;height:53px;border:1px solid #bbb;background:#e4e4e4}
.partner i{position:absolute;left:24px;top:16px;width:36px;height:20px;background:#b5b5b5}
.p-arrow{position:absolute;top:25px;width:20px;height:19px;background:#2b2b2b;display:flex;align-items:center;justify-content:center}

/* footer */
.footer{left:111px;top:1020px;width:554px;height:133px;background:var(--footer)}
.fcol{position:absolute;top:16px}
.fcol h4{font-family:"Open Sans",sans-serif;font-size:9.5px;font-weight:700;color:#fff;margin-bottom:6px}
.fcol li{list-style:none;font-family:"Open Sans",sans-serif;font-weight:400;font-size:7.8px;color:#e0e0e0;height:16px;line-height:15px;border-bottom:1px solid #454545;width:90px;white-space:nowrap}
.fcol li::before{content:"";display:inline-block;width:3px;height:3px;background:var(--orange);margin-right:4px;vertical-align:middle}
.news-text{font-family:"Open Sans",sans-serif;font-size:6.8px;color:#8a8a8a;line-height:9.5px;width:150px}
.field{margin-top:6px;width:158px;height:20px;background:#fff;border-radius:2px;font-size:6.5px;color:#999;padding:6px 7px}
.submit{margin:9px 0 0 110px;width:48px;height:18px;background:var(--navy);color:#fff;font-size:7.5px;font-weight:700;display:flex;align-items:center;justify-content:center;border-radius:2px}
.bottom{left:111px;top:1153px;width:554px;height:47px;background:var(--footer-low);text-align:center}
.bottom .soc{display:flex;justify-content:center;gap:8px;margin-top:9px}
.bottom .soc span{width:9px;height:9px;background:var(--lime);display:block}
.bottom p{font-family:"Open Sans",sans-serif;font-size:6.8px;color:#bcbcbc;margin-top:9px}
</style>
</head>
<body>

<div class="abs topbar">
  <div class="abs contact" style="left:112px">
    <svg width="8" height="8" viewBox="0 0 10 10"><path d="M2 1l2 2-1 1.3c.6 1.2 1.5 2.1 2.7 2.7L7 6l2 2-1.2 1.3C4.5 9 1 5.5.7 2.2z" fill="#d8dee6"/></svg>
    +0800 555 0190
  </div>
  <div class="abs contact" style="left:196px">
    <svg width="9" height="7" viewBox="0 0 10 8"><rect x=".5" y=".5" width="9" height="7" fill="none" stroke="#d8dee6"/><path d="M.5.5l4.5 4 4.5-4" fill="none" stroke="#d8dee6"/></svg>
    hello@supplycircle.example
  </div>
  <div class="abs social"><span></span><span></span><span></span><span></span></div>
</div>

<header class="abs header">
  <div class="abs brand"><span class="mark"></span><span class="name">Clinician Supply Circle</span></div>
  <nav class="abs nav">
    <a class="current" href="#">Home</a>
    <a href="#" style="width:80px">About us</a>
    <a href="#" style="width:60px">Services</a>
    <a href="#" style="width:60px">Blog</a>
    <a href="#" style="width:80px">Contact Us</a>
  </nav>
</header>

<section class="abs hero"></section>
<div class="abs hero-panel">
  <div class="hero-title"><b>HELPING TO</b><span>PROTECT YOUR</span><b>FUTURE TODAY</b></div>
  <p class="hero-text">Donec condimentum ex vel neque vehicula hendrerit. Proin interdum vehicula eleifend. Proin posuere pretium odio, vitae mollis velit sagittis nec.</p>
  <a class="hero-btn" href="#">CLICK HERE TO VIEW MORE
    <svg width="9" height="9" viewBox="0 0 10 10"><circle cx="5" cy="5" r="5" fill="#fff"/><path d="M4 2.8L6.2 5 4 7.2" stroke="#e5780c" stroke-width="1.4" fill="none"/></svg></a>
  <div class="dots"><i></i><i></i><i></i></div>
</div>
<div class="abs hero-photo" role="img" aria-label="Photo of a physician reviewing paperwork with a client at an office desk"></div>

<main class="abs main">
  <section class="welcome">
    <h1>Welcome to Clinician Supply Circle</h1>
    <p style="top:53px">Nam vitae convallis dolor, ut malesuada neque. Curabitur blandit posuere aliquam. Sed porttitor ultricies iaculis. Ut dapibus rutrum lectus. Proin interdum vehicula eleifend. Proin posuere pretium odio, vitae mollis velit sagittis nec. Cras venenatis justo sed ex commodo, ac luctus libero tempus. Curabitur pulvinar luctus eros,</p>
    <p style="top:96px">Ut mattis a est eget luctus. Nulla interdum metus vitae turpis rhoncus, id porta nibh bibendum. Maecenas consequat malesuada arcu sed consectetur. Sed porttitor metus non venenatis dictum. Donec condimentum tristique augue, vel venenatis lectus placerat sit amet.</p>
    <a class="abs more-btn" href="#">View more <span class="ring"></span></a>
  </section>

  <section class="abs services">
    <h2>Our Services</h2>
    <div class="arrow" style="left:0;border-radius:0 12px 12px 0"><svg width="6" height="9" viewBox="0 0 6 9"><path d="M5 1L1.5 4.5 5 8" stroke="#fff" stroke-width="1.5" fill="none"/></svg></div>
    <div class="arrow" style="left:542px;border-radius:12px 0 0 12px"><svg width="6" height="9" viewBox="0 0 6 9"><path d="M1 1l3.5 3.5L1 8" stroke="#fff" stroke-width="1.5" fill="none"/></svg></div>

    <div class="card" style="left:29px">
      <div class="cap" role="img" aria-label="Decorative navy card header"></div>
      <span class="icon"></span><div class="label">DISABILITY<br>INSURANCE</div>
    </div>
    <div class="card hover" style="left:158px">
      <span class="icon" style="opacity:.35"></span><div class="label">LIFE<br>INSURANCE</div>
      <div class="veil"></div>
      <svg width="108" height="116" viewBox="0 0 108 116" style="position:absolute;left:0;top:0">
        <circle cx="40" cy="55" r="3.5" fill="none" stroke="#fff" stroke-width="1.5"/><path d="M42.5 57.5l3 3" stroke="#fff" stroke-width="1.8"/>
        <path d="M67 53l4-4M66 56a2 2 0 0 1 0-3l2-2M72 50a2 2 0 0 1 0 3l-2 2" stroke="#fff" stroke-width="1.3" fill="none"/>
        <path d="M57 78v10l2.5-2 2 4 1.5-.8-2-4h3z" fill="#fff" stroke="#333" stroke-width=".5"/>
      </svg>
    </div>
    <div class="card" style="left:287px">
      <div class="cap" role="img" aria-label="Decorative navy card header"></div>
      <span class="icon"></span><div class="label">RETIREMENT<br>PLANNING</div>
    </div>
    <div class="card" style="left:416px">
      <div class="cap" role="img" aria-label="Decorative navy card header"></div>
      <span class="icon"></span><div class="label">STUDENT LOAN<br>ADVISORS</div>
    </div>
  </section>

  <section class="blog">
    <h2 class="abs col-title" style="left:18px;top:374px">From Blog</h2>
    <div class="post" style="top:406px"><div class="date">September 20, 2014</div><div class="title">Interdum et malesuada</div><div class="text">Donec metus lacus, sagittis id ligula a, porttitor hendrerit nunc. Mauris varius enim...</div></div>
    <div class="post-rule" style="top:461px"></div>
    <div class="post" style="top:469px"><div class="date">September 20, 2014</div><div class="title">Interdum et malesuada</div><div class="text">Donec metus lacus, sagittis id ligula a, porttitor hendrerit nunc. Mauris varius enim...</div></div>
    <div class="post-rule" style="top:523px"></div>
    <div class="post" style="top:536px"><div class="date">September 20, 2014</div><div class="title">Interdum et malesuada</div><div class="text">Donec metus lacus, sagittis id ligula a, porttitor hendrerit nunc. Mauris varius enim...</div></div>
  </section>

  <section class="latest">
    <h2 class="abs col-title" style="left:197px;top:374px">Latest News</h2>
    <div class="news" style="top:403px"><div class="tag">21 oct</div><div class="text">Phasellus fringilla hendrerit lectus nec vehicula. Pellentesque habitant morbi tristique senectus.</div><div class="read">Read more »</div></div>
    <div class="news" style="top:468px"><div class="tag">20 oct</div><div class="text">Aenean nonumy mauris. Phasellus porta. Praes vestibm molestie lacus. Fusce suscipit.</div><div class="read">Read more »</div></div>
    <div class="news" style="top:534px"><div class="tag">19 oct</div><div class="text">Donec tempor libero ut nisl lacinia vel dignissim lacus tristique. Etiam accumsan velit in quam.</div><div class="read">Read more »</div></div>
  </section>

  <aside>
    <div class="promo active" style="top:381px"><h3>CONSULTING SUPPORT</h3><p>Donec metus lacus, sagittis id ligula a,<br>porttitor hendrerit nunc</p></div>
    <div class="promo" style="top:453px"><h3>FINANCIAL INDICATORS</h3><p>Donec metus lacus, sagittis id ligula a,<br>porttitor hendrerit nunc</p></div>
    <div class="promo" style="top:525px"><h3>ASSISTANCE</h3><p>Donec metus lacus, sagittis id ligula a,<br>porttitor hendrerit nunc</p></div>
  </aside>
</main>

<section class="abs partners">
  <div class="p-arrow" style="left:0"><svg width="6" height="9" viewBox="0 0 6 9"><path d="M5 1L1.5 4.5 5 8" stroke="#fff" stroke-width="1.4" fill="none"/></svg></div>
  <div class="partner" style="left:32px"><i></i></div>
  <div class="partner" style="left:132px"><i></i></div>
  <div class="partner" style="left:232px"><i></i></div>
  <div class="partner" style="left:332px"><i></i></div>
  <div class="partner" style="left:432px"><i></i></div>
  <div class="p-arrow" style="left:534px"><svg width="6" height="9" viewBox="0 0 6 9"><path d="M1 1l3.5 3.5L1 8" stroke="#fff" stroke-width="1.4" fill="none"/></svg></div>
</section>

<footer class="abs footer">
  <div class="fcol" style="left:11px"><h4>Site map</h4><ul><li>Home</li><li>About Us</li><li>Services</li><li>Blogs</li><li>Contact Us</li></ul></div>
  <div class="fcol" style="left:133px"><h4>Quick Links</h4><ul><li>Ut pellentesque lorem</li><li>porttitor justo</li><li>fermentum, et iaculis</li><li>orci tempus. Donec</li><li>orci leo, hendrerit ut</li></ul></div>
  <div class="fcol" style="left:263px"><h4>Legal</h4><ul><li>Ut pellentesque lorem</li><li>porttitor justo</li><li>fermentum, et iaculis</li><li>orci tempus. Donec</li></ul></div>
  <div class="fcol" style="left:384px"><h4>Subscribe Newsletter</h4>
    <p class="news-text">Curabitur tempor posuere fermentum. Sed vehicula ultricies urna scelerisque fermentum</p>
    <div class="field">Enter email address</div>
    <div class="submit">Submit</div>
  </div>
</footer>
<div class="abs bottom">
  <div class="soc"><span></span><span></span><span></span><span></span></div>
  <p>Copyright 2014 All rights reserved</p>
</div>

</body>
</html>
```